Business card for a young woman who performs life enhancement activities with people who have developmental disabilities, what used to be called retardation. She wants to focus on the creative part of her work. She has a degree in art and will engage clients in art projects as well as helping them learn to do things like grocery shop, cook meals, set goals, and live independently.

Target Market(s)

Parents, caregivers, guardians, relatives of people with developmental disabilities, meaning they have not developed in their mental capacities.

Industry/Entity Type

Business

Contact Information for Business Card

Bright Harbor Services, Marisa T. Dunlop, 417 362-8094, marisa@marisadunlop.example, Life enhancement services for people with developmental disabilities. No address.

Font styles to use
Serif

Requirements
Must have
• Marisa wants it to have some indication of the art or creative part of her work with clients. But it must also be businesslike so it appeals to the parents. They have to see her as a professional, but she's compassionate and artsy. She wants just her company name on the front. The other information should be on the back.

```html
<!DOCTYPE html>
<html lang="en">
<head>
<meta charset="utf-8">
<title>Bright Harbor Services — Business Card</title>
<link rel="stylesheet" href="https://fonts.googleapis.com/css2?family=Arvo:wght@400;700&display=swap">
<style>
  :root {
    --backdrop: #2f3a45;
    --card: #ffffff;
    --brand-red: #e4252b;
    --brand-navy: #2b3a8f;
    --meadow-pink: #d2559b;
    --meadow-orange: #f0a23c;
    --meadow-green: #8cc34a;
    --meadow-teal: #3aa8c4;
    --photo-light: #e8d2a8;
    --photo-mid: #c9a07e;
    --photo-dark: #6d5a4c;
  }
  * { box-sizing: border-box; margin: 0; padding: 0; }
  html, body {
    width: 1200px; height: 800px; overflow: hidden;
    background: var(--backdrop);
    font-family: "Arvo", Georgia, serif;
  }
  .canvas {
    position: relative; width: 1200px; height: 800px;
    display: flex; align-items: center; justify-content: center; gap: 40px;
  }
  .card {
    position: relative; width: 540px; height: 309px;
    background: var(--card); overflow: hidden;
    box-shadow: 0 6px 18px rgba(0,0,0,.35);
  }
  .brand-name {
    font-family: "Arvo", Georgia, serif; font-weight: 700;
    color: var(--brand-red); line-height: 1.05;
  }
  /* Front */
  .card--front .brand-name {
    position: absolute; left: 38px; top: 70px; font-size: 34px; width: 300px;
  }
  .meadow {
    position: absolute; left: 0; right: 0; bottom: 0; height: 170px;
    background:
      linear-gradient(180deg, rgba(255,255,255,1) 0%, rgba(255,255,255,0) 45%),
      linear-gradient(90deg, var(--meadow-teal) 0%, var(--meadow-pink) 30%, var(--meadow-orange) 60%, var(--meadow-green) 100%);
    opacity: .75;
  }
  /* Back */
  .photo-frame {
    position: absolute; right: 22px; top: 22px; width: 200px; height: 176px;
    border: 4px solid var(--brand-red); background: var(--card); padding: 3px;
  }
  .photo {
    width: 100%; height: 100%;
    background: radial-gradient(circle at 55% 35%, var(--photo-light) 0%, var(--photo-mid) 45%, var(--photo-dark) 100%);
  }
  .contact {
    position: absolute; left: 60px; top: 120px; text-align: center;
  }
  .contact__name {
    color: var(--brand-red); font-weight: 700; font-size: 17px;
    text-transform: uppercase; letter-spacing: .5px;
  }
  .contact__line { color: var(--brand-navy); font-size: 14px; margin-top: 4px; }
  .card--back .brand-name {
    position: absolute; left: 36px; bottom: 52px; font-size: 26px;
  }
  .tagline-band {
    position: absolute; left: 30px; right: 22px; bottom: 22px; height: 22px;
    background: var(--brand-red); color: #fff;
    font-size: 12.5px; font-weight: 700; line-height: 22px; text-align: center;
  }
</style>
</head>
<body>
<main class="canvas">
  <section class="card card--front" aria-label="Card front">
    <div class="brand-name">Bright Harbor Services</div>
    <div class="meadow" role="img" aria-label="Colourful meadow of stylised dotted flowers"></div>
  </section>

  <section class="card card--back" aria-label="Card back">
    <div class="contact">
      <p class="contact__name">Marisa T. Dunlop</p>
      <p class="contact__line">417 362-8094</p>
      <p class="contact__line">marisa@marisadunlop.example</p>
    </div>
    <div class="photo-frame">
      <div class="photo" role="img" aria-label="Photo of Marisa with a smiling client"></div>
    </div>
    <div class="brand-name">Bright Harbor Services</div>
    <div class="tagline-band">Life enhancement services for people with developmental disabilities</div>
  </section>
</main>
</body>
</html>
```